Business Card Design for Kidvale (Hires out childrens play areas)

Looking to have a business card designed for a company we just bought. The company rents out childrens play areas.

I have uploaded a couple of examples of the kind of business card style I like. Here are two more examples:

https://quorvastudio.nz/project/bright-romp-branding/
https://imgvaultcdn.com/design_img/8841052/302917/302917_5518203_8841052_b73e19a2_image.jpg

I think a white card will be best due to all the colours in the logo.

Size we require: 3.75" x 2.25" (horizontally orientated) with a 0.125" bleed

Uploaded is two versions of our logo.

Details for the card:
1. My name: Liam Verster
2. Title: Managing Director
3. Phone no: 021 563 417
4. Email: liam@kidvale.co.nz
5. URL: www.kidvale.co.nz
6. Address:
PO Box 318625
Fernlea, Auckland

Let me know if you need anything else.

Target Market(s)

Hospitals, doctors surgeries, bed shops, etc.

Contact Information for Business Card

Details for the card:
1. My name: Liam Verster
3. Phone no: 021 563 417
5. URL: www.kidvale.co.nz
6. Address:
PO Box 318625
Fernlea, Auckland

Requirements
Should not have
• Not too busy.

```html
<!DOCTYPE html>
<html lang="en">
<head>
<meta charset="utf-8">
<title>Kidvale Business Card</title>
<link rel="stylesheet" href="https://fonts.googleapis.com/css2?family=Patrick+Hand&display=swap">
<style>
  :root {
    --stage: #cbcbcb;
    --page: #ffffff;
    --card: #ffffff;
    --blue: #1a4ff0;
    --red: #ff3510;
    --yellow: #ffe600;
    --title-red: #ff1a1a;
    --accent: #ff7a1a;
  }
  html, body {
    margin: 0;
    width: 1200px;
    height: 800px;
    overflow: hidden;
    background: var(--page);
    font-family: "Patrick Hand", cursive;
  }
  .stage {
    position: absolute;
    left: 0;
    top: 132px;
    width: 1197px;
    height: 535px;
    background: var(--stage);
  }
  .card {
    position: absolute;
    width: 530px;
    height: 343px;
    background: var(--card);
    overflow: hidden;
    box-shadow: 14px 14px 18px rgba(0,0,0,0.45);
  }
  .card--front { left: 37px; top: 98px; }
  .card--back { left: 621px; top: 102px; }

  .corner-art {
    position: absolute;
    left: 0; top: 0;
    width: 88px; height: 92px;
    background: linear-gradient(135deg, var(--blue) 60%, var(--red) 100%);
  }
  .band-art {
    position: absolute;
    left: 0;
    width: 530px;
    background: linear-gradient(to bottom, var(--blue) 0%, var(--red) 35%, var(--red) 100%);
  }
  .band-art--bottom { bottom: 0; height: 56px; }
  .band-art--top {
    top: 0; height: 52px;
    background: linear-gradient(to top, var(--blue) 0%, var(--red) 35%, var(--red) 100%);
  }

  .brand {
    position: absolute;
    display: flex;
    align-items: center;
    gap: 10px;
    color: var(--blue);
    font-size: 62px;
    line-height: 1;
  }
  .brand__dot {
    width: 30px; height: 30px;
    border-radius: 50%;
    background: var(--accent);
  }
  .card--front .brand { left: 250px; top: 36px; }
  .card--back .brand { left: 170px; top: 122px; }

  .person { position: absolute; left: 30px; top: 127px; }
  .person__name { font-size: 27px; color: var(--blue); line-height: 1; margin: 0; }
  .person__title { font-size: 16px; color: var(--title-red); line-height: 1; margin: 1px 0 0 3px; }
  .contact {
    position: absolute;
    font-size: 24px;
    line-height: 24px;
    color: var(--blue);
    margin: 0;
  }
  .contact--lines { left: 31px; top: 188px; }
  .contact--address { right: 25px; top: 212px; text-align: right; }
</style>
</head>
<body>
  <div class="stage">
    <section class="card card--front">
      <div class="corner-art" role="img" aria-label="Layered colourful corner decoration"></div>
      <div class="band-art band-art--bottom" role="img" aria-label="Colourful decorative band along the bottom edge"></div>
      <div class="brand"><span class="brand__dot"></span><span class="brand__name">Kidvale</span></div>
      <div class="person">
        <p class="person__name">Liam Verster</p>
        <p class="person__title">Managing Director</p>
      </div>
      <p class="contact contact--lines">Phone: 021 563 417<br>Email: liam@kidvale.co.nz<br>URL: www.kidvale.co.nz</p>
      <p class="contact contact--address">P.O. Box 318625<br>Fernlea, Auckland</p>
    </section>

    <section class="card card--back">
      <div class="band-art band-art--top" role="img" aria-label="Colourful decorative band along the top edge"></div>
      <div class="band-art band-art--bottom" role="img" aria-label="Colourful decorative band along the bottom edge"></div>
      <div class="brand"><span class="brand__dot"></span><span class="brand__name">Kidvale</span></div>
    </section>
  </div>
</body>
</html>
```